Change an Existing THEME on a Shopify Site

We currently have a Shopify Site that we would like to launch soon. We picked a current theme [Tavel] and have made some basic changes to it but we don't really know what we're doing. We would like a new theme based on this one specifically built for our site. We already brand colours and a logo.

```html
<!DOCTYPE html>
<html lang="en">
<head>
<meta charset="utf-8">
<title>Maple Lid Co — Home</title>
<link href="https://fonts.googleapis.com/css2?family=Archivo:wght@600;700;800&family=Poppins:wght@400;500;600&display=swap" rel="stylesheet">
<style>
:root{
  --orange:#f39a3a;
  --ink:#1c1c1c;
  --muted:#555;
  --cream:#fcf3e6;
  --star:#f0a12a;
  --white:#fff;
}
*{box-sizing:border-box;margin:0;padding:0}
html,body{width:1200px;height:4934px;overflow:hidden}
body{position:relative;background:var(--white);font-family:"Poppins",sans-serif;color:var(--ink)}
.abs{position:absolute}
.heading{font-family:"Archivo",sans-serif;font-weight:700;color:var(--ink)}
.btn{position:absolute;display:flex;align-items:center;justify-content:center;background:var(--orange);color:var(--ink);font-size:14px;font-weight:600;border-radius:3px;box-shadow:0 3px 6px rgba(0,0,0,.18)}
.img{position:absolute}

.announce{top:0;left:0;width:1200px;height:42px;background:var(--orange);display:flex;align-items:center;justify-content:center;font-size:14px}

.hero{top:42px;left:0;width:1200px;height:612px;background:linear-gradient(168deg,#f6f6f8 0%,#e4e4ec 28%,#c9c9dc 46%,#f0a85c 62%,#e76fa3 76%,#7d62d2 88%,#cfd0dc 100%)}
.hero-fade{top:42px;left:0;width:520px;height:612px;background:linear-gradient(90deg,rgba(246,246,248,.95) 0%,rgba(246,246,248,.7) 55%,rgba(246,246,248,0) 100%)}
.locale{top:90px;left:120px;display:flex;align-items:center;gap:8px;font-size:14px}
.brand{top:54px;left:548px;width:104px;height:104px;border-radius:50%;background:#7fcfc7;display:flex;align-items:center;justify-content:center;text-align:center;font-weight:600;font-size:14px;line-height:1.1;color:var(--ink)}
.nav{top:164px;left:0;width:1200px;display:flex;justify-content:center;gap:28px;font-size:14px}
.icons{top:78px;left:876px;display:flex;gap:34px}
.hero-welcome{top:272px;left:117px;font-size:22px}
.hero-title{top:306px;left:117px;font-size:32px}
.hero-btn{top:360px;left:117px;width:145px;height:44px}

.intro{top:738px;left:0;width:1200px;text-align:center;font-size:19px;line-height:33px;color:#333}

.cook-img{top:928px;left:0;width:585px;height:514px;background:radial-gradient(ellipse at 45% 40%,#f3c27a 0%,#c98a45 35%,#7a5a32 65%,#3f4a36 100%)}
.cook-panel{top:928px;left:585px;width:615px;height:514px;background:var(--cream)}
.cook-title{top:1110px;left:599px;font-size:27px}
.cook-text{top:1154px;left:599px;font-size:16px}
.cook-btn{top:1205px;left:599px;width:110px;height:44px}

.products-title{top:1538px;left:0;width:1200px;text-align:center;font-size:40px}
.card-img{width:232px;height:247px;border:1.5px solid #bdbdbd}
.tag{position:absolute;top:12px;left:12px;background:var(--orange);color:var(--white);font-size:9px;padding:3px 10px;border-radius:2px}
.card-vendor{font-size:13px;letter-spacing:.3px}
.card-price{font-size:23px;font-weight:600;font-family:"Archivo",sans-serif}
.stars{color:var(--star);font-size:14px;letter-spacing:1px}
.view-all{top:2427px;left:508px;width:184px;height:46px}

.banner{top:2582px;left:0;width:1200px;height:428px;background:linear-gradient(100deg,#7fa3e0 0%,#e88e86 24%,#f4d27a 46%,#8fb6e8 66%,#e8707e 84%,#f0a060 100%)}
.banner-veil{top:2582px;left:0;width:1200px;height:428px;background:rgba(255,255,255,.32)}
.banner-title{top:2720px;left:0;width:1200px;text-align:center;font-size:29px}
.banner-text{top:2766px;left:0;width:1200px;text-align:center;font-size:17px;color:#333}
.banner-btn{top:2818px;left:549px;width:105px;height:42px}

.reviews-title{top:3086px;left:0;width:1200px;text-align:center;font-size:42px}
.avatar{position:absolute;background:linear-gradient(160deg,#d8b8a0,#6b4a3a)}
.arrow{position:absolute;font-size:22px}
.review-stars{top:3362px;left:0;width:1200px;text-align:center;font-size:20px}
.quote{top:3410px;left:200px;width:800px;text-align:center;font-size:16px;line-height:28px;color:#333}
.reviewer{top:3526px;left:513px;display:flex;align-items:center;gap:18px;font-size:14px;font-weight:600}
.reviewer span.rule{width:42px;height:2px;background:#f2d27a}

.express{top:3634px;left:0;width:1200px;text-align:center;font-size:40px}
.hashtag{top:3704px;left:0;width:1200px;text-align:center;font-size:14px;font-weight:600}
.tile{top:3773px;width:193px;height:195px}

.map{top:4083px;left:0;width:1200px;height:432px;background:linear-gradient(162deg,#f1f1ef 0%,#e9eae6 50%,#cfe6ef 64%,#8fd0ee 74%,#6cc0ea 100%)}
.store{top:4156px;left:40px;width:276px;height:282px;background:var(--white);padding:22px 24px;box-shadow:0 2px 8px rgba(0,0,0,.12)}
.store h3{font-family:"Archivo",sans-serif;font-size:21px;font-weight:700;margin-bottom:14px}
.store .label{font-size:8px;letter-spacing:1px;color:#777;text-transform:uppercase;margin-bottom:4px}
.store p{font-size:10px;line-height:15px;margin-bottom:12px}
.hours{display:grid;grid-template-columns:1fr auto;font-size:10px;row-gap:8px;margin-bottom:18px}
.directions{background:#f7e48a;height:26px;display:flex;align-items:center;justify-content:center;font-size:8px;font-weight:600;letter-spacing:1.5px}
.social-rail{top:4240px;left:12px;display:flex;flex-direction:column;gap:14px}
.dot{width:12px;height:12px;border-radius:50%;background:#333}
.pin{top:4238px;left:592px}

.foot-col h4{font-family:"Archivo",sans-serif;font-size:18px;font-weight:700;margin-bottom:16px}
.foot-col li{list-style:none;font-size:11px;line-height:26px;color:#333}
.subscribe{top:4686px;left:774px;width:344px;border-bottom:1px solid #ccc;padding-bottom:10px;display:flex;justify-content:space-between;font-size:12px}
.sub-note{top:4746px;left:774px;width:330px;font-size:11px;line-height:19px;color:#444}
.foot-social{top:4818px;left:774px;display:flex;gap:32px}
.copyright{top:4886px;left:114px;font-size:12px;color:#444}
.foot-locale{top:4886px;left:878px;display:flex;gap:8px;align-items:center;font-size:12px;color:#444}
.foot-code{top:4886px;left:1114px;font-size:12px;color:#444}
</style>
</head>
<body>

<div class="abs announce">Black Friday Sale: Save up to 60% with code BLACKFRIDAY</div>

<section>
  <div class="img hero" role="img" aria-label="Colourful stacked lidded food storage containers on white steps"></div>
  <div class="abs hero-fade"></div>
  <div class="abs locale">
    <svg width="18" height="18" viewBox="0 0 18 18" fill="none" stroke="#222" stroke-width="1.3"><circle cx="9" cy="9" r="7.5"/><ellipse cx="9" cy="9" rx="3.3" ry="7.5"/><line x1="1.5" y1="9" x2="16.5" y2="9"/></svg>
    United States (USD $)
    <svg width="10" height="8" viewBox="0 0 10 8"><path d="M1 2l4 4 4-4" stroke="#222" stroke-width="1.5" fill="none"/></svg>
  </div>
  <div class="abs brand">Maple<br>Lid Co</div>
  <nav class="abs nav"><span>Home</span><span>Products</span><span>Contact</span></nav>
  <div class="abs icons">
    <svg width="22" height="22" viewBox="0 0 22 22" fill="none" stroke="#222" stroke-width="1.6"><circle cx="9.5" cy="9.5" r="7"/><line x1="14.5" y1="14.5" x2="20" y2="20"/></svg>
    <svg width="22" height="22" viewBox="0 0 22 22" fill="none" stroke="#222" stroke-width="1.6"><path d="M3 3h8l8 8-8 8-8-8z"/><circle cx="7.5" cy="7.5" r="1.3"/></svg>
    <svg width="22" height="22" viewBox="0 0 22 22" fill="none" stroke="#222" stroke-width="1.6"><circle cx="11" cy="7" r="4"/><path d="M3 20c1-5 4-7 8-7s7 2 8 7"/></svg>
    <svg width="22" height="22" viewBox="0 0 22 22" fill="none" stroke="#222" stroke-width="1.6"><path d="M1 3h3l2.5 11h11l2-8H6"/><circle cx="8" cy="18.5" r="1.3"/><circle cx="16" cy="18.5" r="1.3"/></svg>
  </div>
  <div class="abs hero-welcome">Welcome to</div>
  <h1 class="abs heading hero-title">Maple Lid Co</h1>
  <div class="btn hero-btn">View collection</div>
</section>

<p class="abs intro">Your friendly destination for authentic lidded storage and more.<br>From kitchen favorites to family-friendly finds, we're here to make<br>your home more fun, functional, and fabulous.</p>

<section>
  <div class="img cook-img" role="img" aria-label="Baked cookies and pastries beside colourful storage canisters"></div>
  <div class="abs cook-panel"></div>
  <h2 class="abs heading cook-title">Cook and Bake</h2>
  <p class="abs cook-text">Everything you need to prep, mix, and bake like a pro.</p>
  <div class="btn cook-btn">Shop Now</div>
</section>

<section>
  <h2 class="abs heading products-title">Our Products</h2>

  <div class="abs card-img" style="top:1629px;left:117px;background:radial-gradient(circle at 50% 55%,#25bfa4 0%,#8fe0d2 32%,#eef9f7 58%,#fff 72%)" role="img" aria-label="Teal and white stacked storage set"></div>
  <div class="abs card-img" style="top:1629px;left:362px;background:radial-gradient(ellipse at 50% 58%,#2a2a2a 0%,#8a8a8a 30%,#efefef 55%,#fff 70%)" role="img" aria-label="Black kitchen utensil set"><span class="tag">Trending</span></div>
  <div class="abs card-img" style="top:1629px;left:609px;background:linear-gradient(180deg,#fff 8%,#f56a8c 28%,#f6a13a 45%,#f4e14a 60%,#3a7ef0 75%,#52c84a 88%,#fff 96%)" role="img" aria-label="Rainbow nesting bowls"><span class="tag">Trending</span></div>
  <div class="abs card-img" style="top:1629px;left:855px;background:radial-gradient(ellipse at 50% 52%,#4fb8b8 0%,#8fd4d2 32%,#eaf7f7 58%,#fff 72%)" role="img" aria-label="Teal stacking canisters"></div>

  <div class="abs card-img" style="top:2028px;left:117px;background:radial-gradient(ellipse at 50% 52%,#e7e9ee 0%,#d9b9c4 28%,#f4f5f7 55%,#fff 72%)" role="img" aria-label="Clear glass storage containers"></div>
  <div class="abs card-img" style="top:2028px;left:362px;background:radial-gradient(ellipse at 50% 55%,#f56b3a 0%,#c9e83a 30%,#2f7ef0 48%,#f3f7ff 66%,#fff 76%)" role="img" aria-label="Bright lidded bowls"><span class="tag">Trending</span></div>
  <div class="abs card-img" style="top:2028px;left:609px;background:radial-gradient(ellipse at 45% 50%,#2f86d8 0%,#7cb8ea 28%,#e8f2fb 55%,#fff 72%)" role="img" aria-label="Blue measuring scoop"></div>
  <div class="abs card-img" style="top:2028px;left:855px;background:linear-gradient(180deg,#fff 12%,#f24a9a 26%,#2f6ff0 42%,#f6843a 60%,#c8e83a 78%,#fff 92%)" role="img" aria-label="Colourful stacking containers"><span class="tag">Trending</span></div>

  <div class="abs" style="top:1900px;left:117px"><div class="card-vendor">KAENCA CASEICAN</div><div class="card-price">$76.00 USD</div><div class="stars">★★★★★</div></div>
  <div class="abs" style="top:1900px;left:362px"><div class="card-vendor">KAENCA CASEICAN</div><div class="card-price">$76.00 USD</div><div class="stars">★★★★★</div></div>
  <div class="abs" style="top:1900px;left:609px"><div class="card-vendor">KAENCA CASEICAN</div><div class="card-price">$76.00 USD</div><div class="stars">★★★★★</div></div>
  <div class="abs" style="top:1900px;left:855px"><div class="card-vendor">KAENCA CASEICAN</div><div class="card-price">$76.00 USD</div><div class="stars">★★★★★</div></div>
  <div class="abs" style="top:2299px;left:117px"><div class="card-vendor">KAENCA CASEICAN</div><div class="card-price">$76.00 USD</div><div class="stars">★★★★★</div></div>
  <div class="abs" style="top:2299px;left:362px"><div class="card-vendor">KAENCA CASEICAN</div><div class="card-price">$76.00 USD</div><div class="stars">★★★★★</div></div>
  <div class="abs" style="top:2299px;left:609px"><div class="card-vendor">KAENCA CASEICAN</div><div class="card-price">$76.00 USD</div><div class="stars">★★★★★</div></div>
  <div class="abs" style="top:2299px;left:855px"><div class="card-vendor">KAENCA CASEICAN</div><div class="card-price">$76.00 USD</div><div class="stars">★★★★★</div></div>

  <div class="btn view-all">View All Products</div>
</section>

<section>
  <div class="img banner" role="img" aria-label="Close-up of many colourful plastic kitchen containers"></div>
  <div class="abs banner-veil"></div>
  <h2 class="abs heading banner-title">Kcasoei Eaeicjseic Oascisec</h2>
  <p class="abs banner-text">Gansectetur adipiscing elit, sed do eiusmod tempor incididunt ut labore et dolore magna</p>
  <div class="btn banner-btn">Shop Now</div>
</section>

<section>
  <h2 class="abs heading reviews-title">What Clients Are Saying</h2>
  <span class="arrow" style="top:3230px;left:146px">←</span>
  <div class="avatar" style="top:3218px;left:193px;width:52px;height:52px;border-radius:12px;opacity:.6" role="img" aria-label="Customer portrait"></div>
  <div class="avatar" style="top:3208px;left:373px;width:76px;height:76px;border-radius:18px" role="img" aria-label="Customer portrait"></div>
  <div class="avatar" style="top:3182px;left:541px;width:128px;height:128px;border-radius:28px" role="img" aria-label="Customer portrait"></div>
  <div class="avatar" style="top:3208px;left:760px;width:76px;height:76px;border-radius:18px" role="img" aria-label="Customer portrait"></div>
  <div class="avatar" style="top:3218px;left:963px;width:52px;height:52px;border-radius:12px;opacity:.6" role="img" aria-label="Customer portrait"></div>
  <span class="arrow" style="top:3230px;left:1040px">→</span>
  <div class="abs review-stars stars">★★★★★</div>
  <p class="abs quote">Gadsectetur adipiscing elit, sed do eiusmod tempor incididunt ut labore et dolore magna aliqua. Ut enim ad minim veniam, quis nostrud exercitation ullamco laboris nisi ut aliquip ex ea commodo consequat. Duis aute irure dolor in reprehenderit in voluptate velit esse cillum.</p>
  <div class="abs reviewer"><span class="rule"></span>Jonah Pellar</div>
</section>

<section>
  <h2 class="abs heading express">Express yourself with</h2>
  <div class="abs hashtag">#MapleLidCo</div>
  <div class="img tile" style="left:119px;background:radial-gradient(circle at 45% 45%,#6fdc52 0%,#a9e98e 40%,#eef4ec 80%)" role="img" aria-label="Green lidded container"></div>
  <div class="img tile" style="left:312px;background:linear-gradient(180deg,#f4f6f8 20%,#3a7ee0 40%,#f0b030 58%,#e2483a 74%,#eef0f2 92%)" role="img" aria-label="Stacked colourful containers"></div>
  <div class="img tile" style="left:505px;background:linear-gradient(180deg,#151515 0%,#2a2a2a 35%,#c9ccd2 65%,#eef0f2 100%)" role="img" aria-label="Clear containers on dark shelf"></div>
  <div class="img tile" style="left:698px;background:linear-gradient(160deg,#2a7ae8 0%,#d85ad8 45%,#f248a8 70%,#8a3ee0 100%)" role="img" aria-label="Bright stacked boxes"></div>
  <div class="img tile" style="left:891px;background:linear-gradient(180deg,#a85a44 0%,#6a3a30 50%,#2e2220 100%)" role="img" aria-label="Hanging kitchen utensils on brick wall"></div>
</section>

<section>
  <div class="img map" role="img" aria-label="Street map of the store neighbourhood by the harbour"></div>
  <svg class="abs pin" width="18" height="26" viewBox="0 0 18 26"><path d="M9 0C4 0 0 4 0 9c0 7 9 17 9 17s9-10 9-17c0-5-4-9-9-9z" fill="#111"/><circle cx="9" cy="9" r="3.5" fill="#fff"/></svg>
  <div class="abs social-rail"><span class="dot"></span><span class="dot"></span><span class="dot"></span><span class="dot"></span></div>
  <div class="abs store">
    <h3>Find Our Store</h3>
    <div class="label">Address</div>
    <p>418 Harbour Lane<br>Lakeside, ON L2K 4B9, Canada</p>
    <div class="label">Opening hours</div>
    <div class="hours">
      <span>Mon - Fri</span><span>8:30am - 10:30pm</span>
      <span>Saturday</span><span>8:30am - 10:30pm</span>
      <span>Sunday</span><span>8:30am - 10:30pm</span>
    </div>
    <div class="directions">GET DIRECTIONS</div>
  </div>
</section>

<footer>
  <div class="abs foot-col" style="top:4640px;left:119px"><h4>Quick Links</h4><ul><li>Home</li><li>Products</li><li>Contact</li></ul></div>
  <div class="abs foot-col" style="top:4640px;left:323px"><h4>Links</h4><ul><li>About Us</li><li>Terms of Service</li><li>Privacy Policy</li><li>Shipping &amp; Returns</li><li>Cookies</li></ul></div>
  <div class="abs foot-col" style="top:4640px;left:524px"><h4>Support</h4><ul><li>My Account</li><li>Careers</li><li>Contact</li><li>FAQ</li><li>Store locator</li></ul></div>
  <div class="abs foot-col" style="top:4640px;left:774px"><h4>Exclusive Benefits</h4></div>
  <div class="abs subscribe"><span>Enter Email Here</span><span>→</span></div>
  <p class="abs sub-note">Apply for our free membership to receive exclusive deals, news, and events.</p>
  <div class="abs foot-social"><span class="dot"></span><span class="dot"></span><span class="dot"></span><span class="dot"></span></div>
  <div class="abs copyright">© 2025 .All rights reserved.</div>
  <div class="abs foot-locale">
    <svg width="16" height="16" viewBox="0 0 18 18" fill="none" stroke="#444" stroke-width="1.3"><circle cx="9" cy="9" r="7.5"/><ellipse cx="9" cy="9" rx="3.3" ry="7.5"/><line x1="1.5" y1="9" x2="16.5" y2="9"/></svg>
    United States (USD $) ⌄
  </div>
  <div class="abs foot-code">C44</div>
</footer>

</body>
</html>
```